Banner Design Childcare Centre Landscape Orientation

Design a 3000 x 1500mm landscape orientation(using attached template Template - Outdoor-Banner-Large-1500x3000_PORTRAIT ***But please change to landscape orientation) to include these information:

Logo

Slogan = Empowering tomorrow's leaders with confidence, independence, creativity and a strong passion for learning.

- Ages 6 weeks to 6 years
- STEAM based educational programs with a focus on the Montessori method

Now Enrolling
www.brightowlcare.com.au
02 74215096
17 Garnet Lane, Wattlebrook NSW 2198

***Please also include a qr code on the design that directs to www.brightowlcare.com.au
____________________________

About us:

Main Colour Scheme (can add other colours to make it appealing)
The colour scheme for our brand will be HEX #FFFFFF (white), #000000 (black), #F7931A (orange) , #4D4D4D (grey), #00AEFF (blue), #00CAFE (lighter blue).

- Our Mission
The mission of Bluegum Early Learning Academy is to be a leading educational academy for students of infant, toddler and preschool age (1-6 years old). We aim to promote confidence, independence, responsibility, creativity and a strong passion for learning via STEAM (Science, Technology, Engineering, Arts and Mathematics) based education built on a foundation of Montessori principles.

Why STEAM based education via Montessori Principles
Why STEAM based education?

The development of critical thinking skills in students is crucial to preparing them for the challenges of the future. Encouraging students of all ages to think deeply and approach problems with a creative and innovative mindset is essential to fostering the next generation of leaders, innovators, and educators. The integration of Science, Technology, Engineering, Art, and Mathematics (STEAM) in education provides students with a well-rounded and hands-on approach to learning, inspiring them to think more broadly and solve problems with a real-world focus.

Through the implementation of STEAM-based education, students can progress from project-based learning, where they collaborate to explore and discover, to problem-based learning, where they focus on real-world challenges, and ultimately to place-based learning, where they learn by doing. This approach ensures that students are not only gaining knowledge and skills, but also developing their ability to think critically and creatively.

It is equally important to emphasise the role of the arts in education, as creativity and innovation are key components of the future workforce. By providing opportunities for students to apply their knowledge and skills in practical and applicable ways, the arts can support STEAM-based education and ensure that all students are ready to face the challenges ahead.

STEAM-based education provides a comprehensive and hands-on approach to learning, equipping students with the critical thinking and problem-solving skills they will need to succeed in the future. Every child should have the opportunity to develop their creative and innovative abilities, regardless of their career path, and STEAM education is an effective means of achieving this goal.

Why focus on the Montessori Method?

The Montessori Method provides a comprehensive approach to child development and education, offering numerous benefits for children who are raised within its principles. This method is well known for its individualised approach to learning, which allows students to progress at their own pace, and its focus on fostering independence.

In addition to these well-established benefits, the Montessori Method also places a strong emphasis on empathy, social justice, and a lifelong love of learning. By providing children with the freedom and support to question, explore, and make connections, Montessori students develop into confident, enthusiastic, and self-directed learners. They acquire the critical thinking, collaboration, and boldness that are vital skills for children to be well-rounded, confident, and effective leaders in the 21st century.

Industry/Entity Type

Childcare centre

Requirements
Must have
• Landscape orientation (1500 high, 3000 wide)

```html
<!DOCTYPE html>
<html lang="en">
<head>
<meta charset="utf-8">
<title>Bluegum Early Learning Academy – Now Enrolling Banner</title>
<link rel="stylesheet" href="https://fonts.googleapis.com/css2?family=Fredoka:wght@700&family=Poppins:wght@600;700&family=Quicksand:wght@500;600&display=swap">
<style>
  :root{
    --navy:#0b3262;
    --orange:#f7931a;
    --sky:#4fb3f0;
    --light-blue:#00caff;
    --yellow:#f7e55b;
    --white:#ffffff;
    --page:#e4e4e4;
    --photo-a:#d9cfc4;
    --photo-b:#9fd6d0;
  }
  html,body{margin:0;padding:0;overflow:hidden}
  body{width:1200px;height:755px;background:var(--page);position:relative}
  .banner{
    position:absolute;left:0;top:77px;
    width:1216px;height:608px;
    transform:scale(0.98684);transform-origin:0 0;
    background:var(--navy);overflow:hidden;
  }
  .banner-art{position:absolute;inset:0}
  .headline{position:absolute;left:44px;top:78px;margin:0;line-height:1}
  .headline .line-orange,.headline .line-blue{
    display:block;font-family:"Fredoka",sans-serif;font-weight:700;
    font-size:86px;letter-spacing:0;line-height:72px;
  }
  .headline .line-orange{color:var(--orange)}
  .headline .line-blue{color:var(--sky)}
  .headline .line-white{
    display:block;margin-top:6px;font-family:"Poppins",sans-serif;font-weight:600;
    font-size:40px;color:var(--white);letter-spacing:.3px;line-height:46px;
  }
  .rule{position:absolute;left:44px;top:277px;width:550px;height:2px;background:var(--white)}
  .subline{
    position:absolute;left:44px;top:289px;width:560px;margin:0;
    font-family:"Quicksand",sans-serif;font-weight:500;font-size:25px;line-height:27px;color:var(--white);
  }
  .ages{
    position:absolute;left:96px;top:370px;margin:0;
    font-family:"Poppins",sans-serif;font-weight:700;font-size:33px;line-height:38px;color:var(--white);
    letter-spacing:.3px;
  }
  .programs{
    position:absolute;left:153px;top:435px;margin:0;width:545px;
    font-family:"Quicksand",sans-serif;font-weight:600;font-size:21px;line-height:25px;color:var(--white);
  }
  .brand{
    position:absolute;left:52px;top:476px;width:96px;text-align:center;
    font-family:"Quicksand",sans-serif;font-weight:600;font-size:13px;line-height:15px;color:var(--orange);
  }
  .brand .dot{display:block;width:30px;height:30px;border-radius:50%;background:var(--orange);margin:0 auto 6px}
  .contact{
    position:absolute;left:155px;top:501px;margin:0;
    font-family:"Quicksand",sans-serif;font-weight:600;font-size:22px;color:var(--white);
  }
  .contact-row{display:flex;align-items:center;height:31px;white-space:nowrap}
  .contact-row svg{flex:none;margin-right:8px}
  .contact .phone{font-family:"Poppins",sans-serif;font-weight:700;font-size:21px;margin-right:12px}
  .enroll-badge{
    position:absolute;left:655px;top:133px;width:234px;height:234px;border-radius:50%;
    background:var(--white);display:flex;align-items:center;justify-content:center;
  }
  .enroll-badge .ring{
    width:218px;height:218px;border-radius:50%;background:var(--navy);
    display:flex;align-items:center;justify-content:center;
  }
  .enroll-badge .core{
    width:200px;height:200px;border-radius:50%;background:var(--orange);
    display:flex;flex-direction:column;align-items:center;justify-content:center;color:var(--white);
    font-family:"Poppins",sans-serif;font-weight:700;text-align:center;
  }
  .enroll-badge .now{font-size:66px;line-height:62px;margin-top:6px}
  .enroll-badge .enrolling{font-size:26px;line-height:34px;letter-spacing:.5px}
</style>
</head>
<body>
<main class="banner">
  <svg class="banner-art" width="1216" height="608" viewBox="0 0 1216 608">
    <defs>
      <linearGradient id="classroomTone" x1="0" y1="0" x2="1" y2="1">
        <stop offset="0" stop-color="var(--photo-a)"/>
        <stop offset="0.55" stop-color="#e8e2da"/>
        <stop offset="1" stop-color="var(--photo-b)"/>
      </linearGradient>
    </defs>
    <path class="blob-sky" d="M0,0 H185 C160,20 130,15 105,35 C80,60 50,70 0,72 Z" fill="var(--sky)"/>
    <path class="blob-orange" d="M0,565 C10,548 35,545 55,556 C75,566 92,572 120,585 C140,595 150,600 155,608 H0 Z" fill="var(--orange)"/>
    <circle class="blob-sun" cx="540" cy="10" r="50" fill="var(--yellow)"/>
    <rect role="img" aria-label="Storybook illustration" x="262" y="4" width="86" height="52" rx="6" transform="rotate(-25 305 30)" fill="var(--orange)"/>
    <rect role="img" aria-label="Crayons illustration" x="392" y="2" width="40" height="60" rx="8" fill="#1f5a9a"/>
    <circle role="img" aria-label="Atom illustration" cx="522" cy="584" r="28" fill="#1f5a7a"/>
    <rect role="img" aria-label="Pencil illustration" x="288" y="586" width="66" height="12" rx="6" transform="rotate(25 320 592)" fill="#e2a53a"/>
    <circle role="img" aria-label="Flask illustration" cx="108" cy="590" r="16" fill="var(--yellow)"/>
    <path role="img" aria-label="Photo of toddlers playing with stacking toys at a classroom table with a teacher"
      d="M590,0 C575,70 630,125 720,142 L820,160 L820,330 L762,372 C752,460 840,560 940,608 H1216 V0 Z"
      fill="url(#classroomTone)"/>
    <path class="photo-edge" d="M590,0 C575,70 630,125 720,142 M762,372 C752,460 840,560 940,608"
      fill="none" stroke="var(--sky)" stroke-width="6"/>
    <path class="dash-trail" d="M625,25 C620,80 680,125 760,145 M735,420 C750,500 800,560 848,608"
      fill="none" stroke="var(--white)" stroke-width="1.5" stroke-dasharray="5 5"/>
    <ellipse role="img" aria-label="Paint palette illustration" cx="745" cy="580" rx="50" ry="34" fill="#f3e7d3"/>
    <path class="brush-band" fill="var(--orange)"
      d="M48,362 L120,358 L260,361 L420,357 L560,360 L600,362 L594,370 L613,376 L600,384 L610,392 L598,400 L606,410 L560,414 L420,411 L260,414 L120,411 L52,413 L60,404 L38,398 L56,390 L44,381 L58,372 Z"/>
  </svg>

  <h1 class="headline">
    <span class="line-orange">EMPOWERING</span>
    <span class="line-blue">TOMORROW’S</span>
    <span class="line-white">LEADERS WITH CONFIDENCE</span>
  </h1>
  <div class="rule"></div>
  <p class="subline">independence, creativity and a strong passion for learning</p>

  <p class="ages">AGES 6 WEEKS TO 6 YEARS</p>

  <p class="programs">STEAM based educational programs with a focus on the Montessori method</p>

  <div class="brand"><span class="dot"></span>Bluegum Early Learning Academy</div>

  <div class="contact">
    <div class="contact-row">
      <svg width="16" height="16" viewBox="0 0 24 24"><path d="M6.6 10.8a15.1 15.1 0 006.6 6.6l2.2-2.2a1 1 0 011-.25 11.4 11.4 0 003.6.6 1 1 0 011 1V20a1 1 0 01-1 1A17 17 0 013 4a1 1 0 011-1h3.5a1 1 0 011 1 11.4 11.4 0 00.6 3.6 1 1 0 01-.25 1z" fill="var(--yellow)"/></svg>
      <span class="phone">02 74215096</span>
      <svg width="14" height="18" viewBox="0 0 24 30"><path d="M12 0a9 9 0 00-9 9c0 7 9 15 9 15s9-8 9-15a9 9 0 00-9-9zm0 12.5A3.5 3.5 0 1112 5.5a3.5 3.5 0 010 7z" fill="var(--yellow)"/><rect x="3" y="26" width="18" height="3" rx="1.5" fill="var(--yellow)"/></svg>
      <span class="address">17 Garnet Lane, Wattlebrook NSW 2198</span>
    </div>
    <div class="contact-row">
      <svg width="17" height="17" viewBox="0 0 24 24"><circle cx="12" cy="12" r="10" fill="none" stroke="var(--yellow)" stroke-width="2"/><path d="M2 12h20M12 2c3 3 3 17 0 20M12 2c-3 3-3 17 0 20" fill="none" stroke="var(--yellow)" stroke-width="2"/></svg>
      <span class="web">www.brightowlcare.com.au</span>
    </div>
  </div>

  <div class="enroll-badge">
    <div class="ring">
      <div class="core">
        <span class="now">NOW</span>
        <span class="enrolling">ENROLLING</span>
      </div>
    </div>
  </div>
</main>
</body>
</html>
```